Poetry Book Cover Design Project

Looking for a minimalistic book cover design for a collection of poems. The book title is "Where the Lanterns Drift Toward Morning". There are three parts to the book. First covers poetry in the theme of Rage. Second love and desire. The third is strange poems. Essentially the sections are "Rage", "Desire" and the "Strange". The reason for the title "Where the Lanterns Drift Toward Morning" is as if someone is writing these till life changes towards the intended outcome as felt in each poem. I want to have the author's name "Tharusha Wickramasooriya" at the bottom. Ilustration attached.
- Minimalistic

```html
<!DOCTYPE html>
<html lang="en">
<head>
<meta charset="UTF-8">
<title>Where the Lanterns Drift Toward Morning — Tharusha Wickramasooriya</title>
<link rel="stylesheet" href="https://fonts.googleapis.com/css2?family=EB+Garamond:wght@400;700&display=swap">
<style>
  :root {
    --paper: #f4f5f5;
    --title-orange: #f28c4d;
    --author-ink: #0d0d0d;
    --leaf-deep: #4f7a52;
    --leaf-soft: #8fae8e;
  }
  html, body {
    margin: 0;
    padding: 0;
    width: 800px;
    height: 1200px;
    overflow: hidden;
    background: var(--paper);
  }
  .cover {
    position: relative;
    width: 800px;
    height: 1200px;
    background: linear-gradient(180deg, #f3f4f4 0%, #f6f7f7 60%, #f4f5f5 100%);
    overflow: hidden;
  }
  .title {
    position: absolute;
    top: 42px;
    right: 52px;
    margin: 0;
    font-family: "EB Garamond", Georgia, serif;
    font-weight: 400;
    font-size: 118px;
    line-height: 145px;
    color: var(--title-orange);
    text-align: right;
    letter-spacing: -1px;
  }
  .title span { display: block; }
  .eucalyptus-sprig {
    position: absolute;
    left: 10px;
    top: 525px;
    width: 240px;
    height: 675px;
    background:
      radial-gradient(ellipse 50% 30% at 55% 20%, var(--leaf-soft) 0%, rgba(143,174,142,0) 70%),
      radial-gradient(ellipse 45% 45% at 45% 55%, var(--leaf-deep) 0%, rgba(79,122,82,0.55) 45%, rgba(79,122,82,0) 75%),
      radial-gradient(ellipse 40% 30% at 40% 88%, var(--leaf-deep) 0%, rgba(79,122,82,0) 75%);
    opacity: 0.85;
  }
  .author {
    position: absolute;
    left: 196px;
    top: 1062px;
    margin: 0;
    font-family: "EB Garamond", Georgia, serif;
    font-weight: 700;
    font-size: 38px;
    line-height: 1;
    color: var(--author-ink);
    letter-spacing: 0.5px;
    white-space: nowrap;
  }
</style>
</head>
<body>
  <main class="cover">
    <h1 class="title">
      <span>Where</span>
      <span>the</span>
      <span>Lanterns</span>
      <span>Drift</span>
      <span>Toward</span>
      <span>Morning</span>
    </h1>
    <div class="eucalyptus-sprig" role="img" aria-label="Photograph of a eucalyptus sprig with round green leaves rising along the left edge"></div>
    <p class="author">Tharusha Wickramasooriya</p>
  </main>
</body>
</html>
```